Hvac and insulation company needs good looking business card design

We are hvac and insulation company and looking for a new business cards that look to today standards designs

Target Market(s)

homeowners

Industry/Entity Type

Hvac

Contact Information for Business Card

Name: Dorian Velkova
Home comfort consultant
address: 4827 Marrow Ridge Rd #215 Oakland, CA 94611
office: 888-317-5069
cell: 510-642-1388
Lic.# 458127
Email: dorian@quarry-hvac.com
Web: quarry-hvac.com

Requirements
Must have
• clean and sleek look
Nice to have
• simple with a clean look
Should not have
• to busy business card

```html
<!DOCTYPE html>
<html lang="en">
<head>
<meta charset="utf-8">
<title>Quarry Home Solutions – Business Card</title>
<link href="https://fonts.googleapis.com/css2?family=Roboto:wght@400;500&display=swap" rel="stylesheet">
<style>
  :root {
    --bg: #2b2b2d;
    --card: #0d0d0e;
    --card-edge: #1c1c1e;
    --orange: #f3902f;
    --white: #f2f2f2;
    --grey: #bdbdbd;
  }
  * { margin: 0; padding: 0; box-sizing: border-box; }
  html, body { width: 1200px; height: 896px; overflow: hidden; }
  body {
    background: var(--bg);
    font-family: "Roboto", sans-serif;
    display: flex;
    align-items: center;
    justify-content: center;
    gap: 40px;
  }
  .card {
    position: relative;
    width: 540px;
    height: 310px;
    border-radius: 22px;
    background: linear-gradient(135deg, var(--card-edge) 0%, var(--card) 55%);
    box-shadow: 0 18px 40px rgba(0,0,0,.45);
    overflow: hidden;
  }
  .brand {
    display: flex;
    align-items: center;
    gap: 12px;
    color: var(--orange);
    font-weight: 500;
    white-space: nowrap;
  }
  .brand-dot {
    width: 30px; height: 30px;
    border-radius: 50%;
    background: var(--orange);
    flex: none;
  }
  .card-front .brand {
    position: absolute;
    top: 50%; left: 50%;
    transform: translate(-50%, -50%);
    font-size: 30px;
  }
  .card-back .brand {
    position: absolute;
    top: 58px; left: 60px;
    font-size: 24px;
  }
  .card-back .brand-dot { width: 24px; height: 24px; }
  .license {
    position: absolute;
    top: 30px; right: 34px;
    font-size: 18px;
    color: var(--white);
  }
  .license span { color: var(--orange); }
  .contact {
    position: absolute;
    left: 44px; bottom: 26px;
  }
  .contact-marker {
    position: absolute;
    left: -22px; top: 4px;
    width: 8px; height: 44px;
    background: var(--orange);
    border-top: 4px solid var(--grey);
  }
  .contact-name {
    color: var(--orange);
    font-size: 19px;
    font-weight: 500;
    text-transform: uppercase;
    letter-spacing: .3px;
  }
  .contact-title {
    color: var(--white);
    font-size: 13.5px;
    margin-bottom: 8px;
  }
  .contact-address {
    color: var(--white);
    font-size: 12.5px;
    line-height: 1.35;
    margin-bottom: 6px;
  }
  .contact-list { list-style: none; }
  .contact-list li {
    display: flex;
    align-items: center;
    gap: 8px;
    color: var(--white);
    font-size: 12.5px;
    line-height: 1.45;
  }
  .contact-list svg { width: 11px; height: 11px; flex: none; }
  .contact-list .accent { color: var(--orange); }
</style>
</head>
<body>
  <section class="card card-front">
    <div class="brand"><span class="brand-dot"></span>Quarry Home Solutions</div>
  </section>

  <section class="card card-back">
    <div class="brand"><span class="brand-dot"></span>Quarry Home Solutions</div>
    <div class="license"><span>Lic.#</span> 458127</div>

    <div class="contact">
      <span class="contact-marker"></span>
      <div class="contact-name">Dorian Velkova</div>
      <div class="contact-title">Home comfort consultant</div>
      <div class="contact-address">4827 Marrow Ridge Rd<br>#215 Oakland, CA 94611</div>
      <ul class="contact-list">
        <li>
          <svg viewBox="0 0 12 12"><path d="M2.5 1h2l1 3-1.3.9a6 6 0 0 0 2.9 2.9L8 6.5l3 1v2c0 .8-.7 1.5-1.5 1.5A8.5 8.5 0 0 1 1 2.5C1 1.7 1.7 1 2.5 1z" fill="var(--orange)"/></svg>
          888-317-5069
        </li>
        <li>
          <svg viewBox="0 0 12 12"><rect x="3" y="0.5" width="6" height="11" rx="1.2" fill="none" stroke="var(--orange)" stroke-width="1.3"/><circle cx="6" cy="9.5" r=".7" fill="var(--orange)"/></svg>
          510-642-1388
        </li>
        <li>
          <svg viewBox="0 0 12 12"><rect x="0.8" y="2" width="10.4" height="8" rx="1" fill="none" stroke="var(--orange)" stroke-width="1.2"/><path d="M1 2.5 6 6.5l5-4" fill="none" stroke="var(--orange)" stroke-width="1.2"/></svg>
          dorian@quarry-hvac.com
        </li>
        <li>
          <svg viewBox="0 0 12 12"><circle cx="6" cy="6" r="5" fill="none" stroke="var(--orange)" stroke-width="1.2"/><ellipse cx="6" cy="6" rx="2.2" ry="5" fill="none" stroke="var(--orange)" stroke-width="1"/><path d="M1 6h10" stroke="var(--orange)" stroke-width="1"/></svg>
          <span>www.<span class="accent">quarry-hvac</span>.com</span>
        </li>
      </ul>
    </div>
  </section>
</body>
</html>
```